DOG DAYCARE BILLBOARD

Design a bold exciting billboard that can be read easily from a distance! Our goal is brand awareness and showcasing the services we offer (Boarding, Grooming, Daycare, and Training.
we would like to see examples with the phrase "your best friend's best day". Our name Bright Meadow Canine Activity Center (or just Bright Meadow might work better and could be bigger) and the services we provide.
(there are two examples of what we like included in the pictures)
you can find more information o our website at pawplayhub@mailnest.example.

```html
<!DOCTYPE html>
<html lang="en">
<head>
<meta charset="utf-8">
<title>Bright Meadow Canine Activity Center – Billboard</title>
<link rel="stylesheet" href="https://fonts.googleapis.com/css2?family=Archivo:wdth,wght@62..125,700..900&display=swap">
<style>
  :root {
    --paper: #f8f9f8;
    --ink: #1d1d1b;
    --green: #47ee06;
    --orange: #f7941d;
    --white: #ffffff;
    --photo-wall: #d9dccf;
    --photo-curtain: #6f9e97;
    --photo-fur: #b3662c;
  }
  * { margin: 0; padding: 0; box-sizing: border-box; }
  html, body {
    width: 1200px;
    height: 644px;
    overflow: hidden;
    background: var(--paper);
  }
  .billboard {
    position: relative;
    width: 1200px;
    height: 644px;
    background: var(--paper);
    font-family: "Archivo", "Arial Black", sans-serif;
    color: var(--ink);
  }
  .services-band {
    position: absolute;
    left: 520px;
    top: 427px;
    width: 680px;
    height: 134px;
    background: var(--green);
  }
  .art {
    position: absolute;
    inset: 0;
    width: 1200px;
    height: 644px;
  }
  .brand-name {
    position: absolute;
    left: 352px;
    top: 36px;
    width: 190px;
    height: 190px;
    display: flex;
    align-items: center;
    justify-content: center;
    text-align: center;
    font-weight: 800;
    font-stretch: 90%;
    font-size: 26px;
    line-height: 1.05;
    color: var(--ink);
  }
  .headline {
    position: absolute;
    right: 29px;
    top: 22px;
    text-align: right;
    font-weight: 900;
    font-stretch: 80%;
    font-size: 88px;
    line-height: 99px;
    white-space: nowrap;
  }
  .headline .accent { color: var(--green); }
  .center-name {
    position: absolute;
    right: 29px;
    top: 348px;
    font-weight: 700;
    font-size: 32px;
    letter-spacing: 1.5px;
    white-space: nowrap;
  }
  .services {
    position: absolute;
    top: 436px;
    left: 590px;
    width: 590px;
    display: grid;
    grid-template-columns: 355px 1fr;
    row-gap: 8px;
    list-style: none;
  }
  .services li {
    display: flex;
    align-items: center;
    gap: 14px;
    font-weight: 700;
    font-size: 43px;
    line-height: 50px;
    color: var(--white);
    letter-spacing: 1px;
  }
  .services li::before {
    content: "";
    width: 20px;
    height: 20px;
    border-radius: 50%;
    background: var(--white);
    flex: none;
  }
  .website {
    position: absolute;
    left: 560px;
    right: 0;
    top: 572px;
    text-align: center;
    font-weight: 700;
    font-size: 38px;
    letter-spacing: 1.5px;
    color: var(--orange);
  }
</style>
</head>
<body>
<main class="billboard">
  <div class="services-band"></div>

  <svg class="art" viewBox="0 0 1200 644" aria-hidden="false">
    <defs>
      <linearGradient id="photoTone" x1="0" y1="0" x2="1" y2="0.3">
        <stop offset="0" stop-color="var(--photo-wall)"/>
        <stop offset="0.45" stop-color="#c79a76"/>
        <stop offset="0.7" stop-color="var(--photo-fur)"/>
        <stop offset="1" stop-color="var(--photo-curtain)"/>
      </linearGradient>
    </defs>
    <path class="photo-area" role="img"
          aria-label="Photo of a smiling woman hugging a golden retriever indoors"
          d="M0 122 C60 90 120 68 190 65 C260 62 320 85 356 113 C410 150 455 190 476 231 C515 300 540 360 549 504 C552 560 540 610 520 644 L0 644 Z"
          fill="url(#photoTone)"/>
    <path class="photo-edge"
          d="M0 122 C60 90 120 68 190 65 C260 62 320 85 356 113 C410 150 455 190 476 231 C515 300 540 360 549 504 C552 560 540 610 520 644"
          fill="none" stroke="var(--orange)" stroke-width="6"/>
    <circle class="brand-badge" cx="447" cy="131" r="95"
            fill="var(--white)" stroke="var(--orange)" stroke-width="6"/>
  </svg>

  <div class="brand-name">Bright<br>Meadow</div>

  <h1 class="headline">
    Your <span class="accent">Best</span><br>
    <span class="accent">Friend’s</span> Best<br>
    Day
  </h1>

  <p class="center-name">Bright Meadow Canine Activity Center</p>

  <ul class="services">
    <li>Boarding</li>
    <li>Grooming</li>
    <li>Daycare</li>
    <li>Training</li>
  </ul>

  <p class="website">brightmeadowplay.example</p>
</main>
</body>
</html>
```